Business card for our large format printing and installation business

We want a professional looking business card for our business. We manufacture and install Signs.

On the back of the card add this info
Large Format Graphics Printing & Installations, Event Graphics, Banners, Posters, Vehicle Fleet Graphics, Boat Wraps, Wall Murals, Decals,Displays,Signs,Plaques,Digital Signs

On the Front of the card add the Tallowfern Signs logo, plus On the back of the card add the Orange Tallowfern Wraps logo. The 2 vector logos are attached to the design brief.

Target Market(s)

Local business owners

Contact Information for Business Card

Colors
f37122
f68d4e
f9ba93

Requirements
Must have
• On the Front of the card add the Tallowfern Signs logo, plus On the back of the card add the Orange Tallowfern Wraps logo. The 2 vector logos are attached to the design brief.

```html
<!DOCTYPE html>
<html lang="en">
<head>
<meta charset="utf-8">
<title>Tallowfern Business Card</title>
<link href="https://fonts.googleapis.com/css2?family=Roboto:wght@400;500;700;900&display=swap" rel="stylesheet">
<style>
  :root {
    --orange: #f39a1e;
    --orange-deep: #f37122;
    --ink: #1c1c1c;
    --card-black: #141414;
    --card-white: #f4f4f4;
    --page: #d9d9d9;
    --text-dark: #222222;
    --text-light: #f2f2f2;
    --rule: #3a3a3a;
  }
  * { box-sizing: border-box; margin: 0; padding: 0; }
  html, body {
    width: 1200px; height: 1021px; overflow: hidden;
    background: var(--page);
    font-family: "Roboto", Arial, sans-serif;
  }
  .card {
    position: absolute;
    left: 220px;
    width: 760px; height: 434px;
    border-radius: 4px;
    box-shadow: 0 6px 18px rgba(0,0,0,0.25);
    overflow: hidden;
  }
  .card-back { top: 50px; background: var(--card-black); }
  .card-front { top: 537px; background: var(--card-white); }

  .services-heading {
    position: absolute; left: 48px; top: 44px;
    color: var(--orange);
    font-weight: 700; font-size: 17px; line-height: 22px;
    text-transform: uppercase; letter-spacing: 0.3px;
  }
  .services-list {
    position: absolute; left: 48px; top: 96px;
    list-style: none;
    color: var(--text-light);
    font-size: 19px; line-height: 25px;
  }
  .services-list li::before {
    content: "•"; color: var(--orange); margin-right: 7px;
  }
  .brand-name {
    position: absolute;
    color: var(--orange);
    font-weight: 900;
    font-size: 46px; line-height: 1;
    letter-spacing: -0.5px;
    text-align: right;
    white-space: nowrap;
  }
  .brand-name span { display: block; }
  .brand-wraps { right: 56px; bottom: 52px; }
  .brand-signs { right: 412px; top: 138px; }

  .divider {
    position: absolute; left: 378px; top: 100px;
    width: 2px; height: 240px; background: var(--rule);
  }
  .contact {
    position: absolute; left: 412px; top: 96px;
    color: var(--text-dark);
  }
  .contact-name { color: var(--orange); font-weight: 500; font-size: 25px; }
  .contact-title { font-size: 19px; margin-bottom: 22px; }
  .contact-address { font-size: 21px; line-height: 26px; margin-bottom: 4px; }
  .contact-line {
    display: flex; align-items: center; gap: 8px;
    font-size: 21px; line-height: 26px;
  }
  .contact-line svg { width: 17px; height: 17px; flex: none; }
</style>
</head>
<body>

<section class="card card-back">
  <h2 class="services-heading">Large Format Graphics<br>Printing &amp; Installations</h2>
  <ul class="services-list">
    <li>Banners</li>
    <li>Posters</li>
    <li>Vehicle Graphics</li>
    <li>Boat Wraps</li>
    <li>Wall Murals</li>
    <li>Decals</li>
    <li>Displays</li>
    <li>Signs</li>
    <li>Plaques</li>
    <li>Digital Signs</li>
  </ul>
  <div class="brand-name brand-wraps"><span>Tallowfern</span><span>Wraps</span></div>
</section>

<section class="card card-front">
  <div class="brand-name brand-signs"><span>Tallowfern</span><span>Signs</span></div>
  <div class="divider"></div>
  <div class="contact">
    <div class="contact-name">Marcus Delgado</div>
    <div class="contact-title">CEO</div>
    <div class="contact-address">1480 Harbor View Lane #7<br>Coral Bend, FL 33120</div>
    <div class="contact-line">
      <svg viewBox="0 0 24 24" aria-hidden="true"><path fill="var(--orange)" d="M6.6 10.8a15.1 15.1 0 0 0 6.6 6.6l2.2-2.2a1 1 0 0 1 1-.25 11.4 11.4 0 0 0 3.6.57 1 1 0 0 1 1 1V20a1 1 0 0 1-1 1A17 17 0 0 1 3 4a1 1 0 0 1 1-1h3.5a1 1 0 0 1 1 1c0 1.250.2 2.45.57 3.57a1 1 0 0 1-.25 1z"/></svg>
      555-014-2290
    </div>
    <div class="contact-line">
      <svg viewBox="0 0 24 24" aria-hidden="true"><path fill="var(--orange)" d="M6.6 10.8a15.1 15.1 0 0 0 6.6 6.6l2.2-2.2a1 1 0 0 1 1-.25 11.4 11.4 0 0 0 3.6.57 1 1 0 0 1 1 1V20a1 1 0 0 1-1 1A17 17 0 0 1 3 4a1 1 0 0 1 1-1h3.5a1 1 0 0 1 1 1c0 1.25.2 2.45.57 3.57a1 1 0 0 1-.25 1z"/></svg>
      555-017-6634 Direct
    </div>
    <div class="contact-line">
      <svg viewBox="0 0 24 24" aria-hidden="true"><rect x="2.5" y="5" width="19" height="14" fill="none" stroke="var(--orange)" stroke-width="2"/><path d="M2.5 5l9.5 8 9.5-8M2.5 19l7-6.5M21.5 19l-7-6.5" fill="none" stroke="var(--orange)" stroke-width="2"/></svg>
      marcus@tallowfern.net
    </div>
    <div class="contact-line">
      <svg viewBox="0 0 24 24" aria-hidden="true"><g fill="none" stroke="var(--orange)" stroke-width="2"><circle cx="12" cy="12" r="9.5"/><ellipse cx="12" cy="12" rx="4" ry="9.5"/><path d="M2.5 12h19M4 7h16M4 17h16"/></g></svg>
      www.tallowfernwraps.com
    </div>
  </div>
</section>

</body>
</html>
```